Corvana Wound Care Business card design

We need a business card designed around our logo which was provided. The logo of preference is the colored. Also the colors and fonts were provided.

Target Market(s)

Our Referral partners are home health agencies.

Industry/Entity Type

Healthcare

Contact Information for Business Card

Name , Phone #, Email , Title

Requirements
Nice to have
• Creativity
Should not have
• basic

```html
<!DOCTYPE html>
<html lang="en">
<head>
<meta charset="UTF-8">
<title>Corvana Wound Care — Business Card</title>
<link href="https://fonts.googleapis.com/css2?family=DM+Serif+Text&family=Lora:wght@400;500;600&display=swap" rel="stylesheet">
<style>
  :root {
    --backdrop: #406b87;
    --royal: #1858a8;
    --navy: #15337a;
    --paper: #eeeff0;
    --ink: #1d1d24;
    --white: #ffffff;
  }
  * { margin: 0; padding: 0; box-sizing: border-box; }
  html, body { width: 1200px; height: 1000px; overflow: hidden; }
  body {
    position: relative;
    background: var(--backdrop);
    font-family: "Lora", Georgia, serif;
  }
  .side-label {
    position: absolute;
    font-family: "DM Serif Text", Georgia, serif;
    color: var(--white);
    font-size: 32px;
    letter-spacing: 3px;
    line-height: 1;
  }
  .side-label--front { left: 293px; top: 68px; }
  .side-label--back { left: 796px; top: 908px; }

  .card {
    position: absolute;
    left: 295px;
    width: 610px;
    height: 348px;
    overflow: hidden;
    box-shadow: 0 6px 14px rgba(0, 0, 0, .25);
  }
  .card--front { top: 125px; background: var(--royal); }
  .card--back { top: 527px; background: var(--paper); }

  .wordmark {
    position: absolute;
    display: flex;
    align-items: center;
    gap: 14px;
    font-family: "DM Serif Text", Georgia, serif;
    white-space: nowrap;
    line-height: 1;
  }
  .wordmark__square { display: block; flex: none; }
  .card--front .wordmark {
    left: 50%; top: 50%;
    transform: translate(-50%, -50%);
    color: var(--white);
    font-size: 44px;
  }
  .card--front .wordmark__square { width: 30px; height: 30px; background: var(--white); border-radius: 4px; }
  .card--back .wordmark {
    left: 28px; top: 48px;
    color: var(--navy);
    font-size: 30px;
  }
  .card--back .wordmark__square { width: 22px; height: 22px; background: var(--navy); border-radius: 3px; }

  .holder { position: absolute; left: 29px; top: 136px; }
  .holder__name {
    font-family: "DM Serif Text", Georgia, serif;
    font-size: 31px;
    letter-spacing: .5px;
    color: var(--navy);
    line-height: 1;
  }
  .holder__title { font-size: 15px; color: var(--ink); margin-top: 6px; letter-spacing: .4px; line-height: 1.1; }
  .divider {
    position: absolute; left: 0; top: 193px;
    width: 238px; height: 1.5px; background: var(--navy);
  }
  .contacts { position: absolute; left: 29px; top: 209px; list-style: none; }
  .contacts li {
    display: flex; align-items: center; gap: 12px;
    font-size: 12.5px; color: var(--ink); height: 20.5px; line-height: 1;
  }
  .contacts svg { width: 15px; height: 15px; fill: none; stroke: var(--navy); stroke-width: 1.5; flex: none; }
  .web { position: absolute; left: 29px; top: 271px; font-size: 12.5px; line-height: 1; color: var(--navy); font-weight: 500; }
  .area { position: absolute; left: 29px; top: 290px; font-size: 11.5px; color: var(--ink); line-height: 1.5; }
  .accent-band {
    position: absolute; right: 0; top: 68px;
    width: 182px; height: 280px;
    background: var(--navy);
    border-radius: 26px 0 0 0;
  }
</style>
</head>
<body>
  <div class="side-label side-label--front">FRONT</div>

  <section class="card card--front">
    <div class="wordmark"><span class="wordmark__square"></span>Corvana Wound Care</div>
  </section>

  <section class="card card--back">
    <div class="wordmark"><span class="wordmark__square"></span>Corvana Wound Care</div>

    <div class="holder">
      <div class="holder__name">Lorem Ipsum</div>
      <div class="holder__title">Managing Director</div>
    </div>
    <div class="divider"></div>

    <ul class="contacts">
      <li>
        <svg viewBox="0 0 16 16"><path d="M3 2h3l1.5 3.5-2 1.3a8 8 0 0 0 3.7 3.7l1.3-2L14 10v3a1 1 0 0 1-1 1A11 11 0 0 1 2 3a1 1 0 0 1 1-1z"/></svg>
        555-014-2290
      </li>
      <li>
        <svg viewBox="0 0 16 16"><rect x="4" y="1.5" width="8" height="4"/><rect x="1.5" y="5.5" width="13" height="6" rx="1"/><rect x="4" y="9.5" width="8" height="5"/></svg>
        555-014-7731
      </li>
      <li>
        <svg viewBox="0 0 16 16"><rect x="1.5" y="3" width="13" height="10"/><path d="M1.5 3.5 8 9l6.5-5.5"/></svg>
        info@corvanacare.com
      </li>
    </ul>
    <div class="web">www.corvanacare.com</div>
    <div class="area">Harlow, Brenton, Ashby<br>&amp; Calder Counties</div>

    <div class="accent-band"></div>
  </section>

  <div class="side-label side-label--back">BACK</div>
</body>
</html>
```